Employees at R&T Gale Power Services need new modern business cards

We need new business cards that showcase our new rebranded logo. We are seeking modern, clean, fresh, attractive cards while still being professional. We want to stand out. A little bit about us: we work in Canada and the USA. We offer Technical Field Advisors to support wind turbine manufacturers through the construction phase of wind farms. I am attaching a mock inspiration picture to lead you in the direction we want to see this go. Also, FYI We have approx. 10/11 different employees that would need their own card. Let me know when you would need everyone's name. We would love to see some black and white options as well as color copies- when using colors we want green to be the dominant color with accents for blue and orange (colors should match our logo). I have also attached copies of our old business card for reference.

Contact Information for Business Card

Name, Telephone, Email, address, company name, website. EXAMPLE: Dean Whitlock, DeanWhitlock@randtgale.net, 555-384-9162, 318276 Fallow Line #7, Marrowby, ON X9Z 4Q2, www.randtgale.net

Colors
0054AA
0677BA
7BADD7
CADEEF
E8F1F8
00AB8E
00BBA5
67D7C9
C6EFE9
E9F9F6
F0912C
F2A743
F7CA91
FBE8D2
FDF5EE

Requirements
Must have
• 2 sided business card

```html
<!DOCTYPE html>
<html lang="en">
<head>
<meta charset="utf-8">
<title>R&amp;T Gale Power Services – Business Card</title>
<link href="https://fonts.googleapis.com/css2?family=Michroma&family=Open+Sans:wght@400&display=swap" rel="stylesheet">
<style>
  :root {
    --bg: #aaaaaa;
    --white: #ffffff;
    --green: #1ea92f;
    --green-deep: #17a832;
    --blue: #2a8fc9;
    --orange: #f6b21c;
    --orange-soft: #f7ca91;
    --text-dark: #111111;
    --text-grey: #6b6b6b;
    --role: #f2a743;
    --icon-blue: #0677ba;
  }
  * { margin: 0; padding: 0; box-sizing: border-box; }
  html, body { width: 1200px; height: 1000px; overflow: hidden; }
  body { background: var(--bg); position: relative; font-family: "Open Sans", Arial, sans-serif; }

  .card {
    position: absolute;
    left: 294px;
    width: 613px;
    height: 351px;
    border-radius: 28px;
    overflow: hidden;
  }

  /* Front */
  .card--front {
    top: 118px;
    background:
      linear-gradient(160deg, rgba(246,178,28,1) 0%, rgba(246,178,28,0) 45%),
      linear-gradient(200deg, var(--green-deep) 35%, #1a9a8a 70%, var(--blue) 88%, #3aa58c 100%);
  }
  .front-decor {
    position: absolute;
    left: -40px; top: -20px;
    width: 330px; height: 400px;
    border-radius: 50%;
    background: radial-gradient(circle at 45% 45%, rgba(255,255,255,0.25), rgba(255,255,255,0) 70%);
  }
  .front-mark {
    position: absolute;
    left: 400px; top: 99px;
    width: 86px; height: 86px;
    border-radius: 50%;
    border: 6px solid var(--white);
  }
  .front-name {
    position: absolute;
    left: 300px; top: 214px;
    width: 287px;
    text-align: center;
    font-family: "Michroma", "Arial Black", sans-serif;
    color: var(--white);
    line-height: 1;
  }
  .front-name .line-main { display: block; font-size: 23px; letter-spacing: 1px; }
  .front-name .line-sub { display: block; font-size: 14px; letter-spacing: 1.5px; margin-top: 6px; }

  /* Back */
  .card--back {
    top: 532px;
    background: var(--white);
  }
  .back-decor {
    position: absolute;
    left: 336px; top: 0;
    width: 277px; height: 351px;
    background:
      radial-gradient(circle at 65% 50%, rgba(255,255,255,1) 0 14%, rgba(255,255,255,0) 15%),
      linear-gradient(170deg, rgba(251,232,210,1) 0%, rgba(247,202,145,0.9) 30%, rgba(198,239,233,0.6) 50%, rgba(123,173,215,0.7) 75%, rgba(202,222,239,0.8) 100%);
    border-top-left-radius: 60% 45%;
    border-bottom-left-radius: 40% 40%;
  }
  .brand {
    position: absolute;
    left: 50px; top: 66px;
    display: flex; align-items: center; gap: 10px;
  }
  .brand-dot {
    width: 56px; height: 56px; border-radius: 50%;
    background: var(--green);
  }
  .brand-name {
    font-family: "Michroma", "Arial Black", sans-serif;
    color: var(--green);
    line-height: 1;
  }
  .brand-name .line-main { display: block; font-size: 17px; letter-spacing: 0.5px; }
  .brand-name .line-sub { display: block; font-size: 10px; letter-spacing: 1px; margin-top: 4px; }

  .person { position: absolute; left: 50px; top: 160px; }
  .person-name { font-size: 24px; color: var(--text-dark); letter-spacing: 0.3px; line-height: 1.1; }
  .person-role { font-size: 17px; color: var(--role); margin-left: 2px; line-height: 1.3; }

  .contacts { position: absolute; left: 52px; top: 238px; list-style: none; }
  .contacts li {
    display: flex; align-items: center; gap: 6px;
    font-size: 17px; color: var(--text-grey);
    height: 27px; letter-spacing: 0.2px;
  }
  .contacts svg { width: 12px; height: 12px; flex: none; }
</style>
</head>
<body>

  <section class="card card--front" aria-label="Card front">
    <div class="front-decor" role="img" aria-label="Faint large brand decoration"></div>
    <div class="front-mark"></div>
    <h1 class="front-name">
      <span class="line-main">R&amp;T GALE POWER</span>
      <span class="line-sub">SERVICES</span>
    </h1>
  </section>

  <section class="card card--back" aria-label="Card back">
    <div class="back-decor" role="img" aria-label="Soft coloured brand decoration"></div>

    <div class="brand">
      <span class="brand-dot"></span>
      <div class="brand-name">
        <span class="line-main">R&amp;T GALE POWER</span>
        <span class="line-sub">SERVICES</span>
      </div>
    </div>

    <div class="person">
      <p class="person-name">Dean Whitlock</p>
      <p class="person-role">Owner</p>
    </div>

    <ul class="contacts">
      <li>
        <svg viewBox="0 0 12 12" aria-hidden="true"><path fill="#0677ba" d="M2.5 0.8l2 2-1 1.3c.6 1.5 1.8 2.7 3.3 3.3l1.3-1 2 2-1.2 1.8C5.5 10 2 6.5 .8 2z"/></svg>
        555-384-9162
      </li>
      <li>
        <svg viewBox="0 0 12 12" aria-hidden="true"><rect x="0.5" y="2.5" width="11" height="7.5" fill="#f6b21c"/><path d="M0.5 2.5l5.5 4 5.5-4" fill="none" stroke="#fff" stroke-width="1"/></svg>
        deanwhitlock@randtgale.net
      </li>
      <li>
        <svg viewBox="0 0 12 12" aria-hidden="true"><circle cx="6" cy="6" r="5.5" fill="#1ea92f"/><path d="M0.5 6h11M6 .5v11M2 3h8M2 9h8" stroke="#fff" stroke-width="0.8" fill="none"/><ellipse cx="6" cy="6" rx="2.5" ry="5.5" fill="none" stroke="#fff" stroke-width="0.8"/></svg>
        www.randtgale.net
      </li>
    </ul>
  </section>

</body>
</html>
```